QT482 - Guard, Track, Tune, Steer - OT Cyber Security Software, KPI Visualisation Software and

Build Website - we require a website with approx 5 tabs on scrolling pane screen - Home, Who We are, Cyber Security, Visualisation, Trusted Partners, Support, Contact, single scrolling panel or tab click to page with images and 2-3 paragraphs of text - wording and links to partners will be provided along with company logo

Target Market(s)

Process Control Markets - Oil and Gas clients, Telecommunications Operators, IOT companies, manufacturing, transport sector etc

Industry/Entity Type

Security

Coding

Coded - Design and coding required

Number of Pages Required

5+ page

Font styles to use
Sans Serif

Colors
0255a3
3176b5
85abd2
f04a50
ec1f27
1b1b1b
474747
919191
d3d3d3

Requirements
Must have
• Scrolling pane / page with tabs along the top -
• Who We are - software and professional services provider for Process Control Cyber Security and Data visualisation
• Guard Track Tune Steer -
• define and defend process control networks, measure, manage, visualise data sets from any source etc
• Process Control Cyber Security - images and wording - area for wording can be created and left to be fully populated etc
• Visualisation - data set visualisation from desk top / tablet / mobile device,
• Trusted Partners - links to www.brevanix.example www.lumicore.example www.dorvale.example.au
• Support
• Contact Details
• images for cyber security risks etc
• data visualisation / visual KPI - software package
• Support - link to www.dorvale.example.au for NOC and Customer Support - sections for Gold, Silver and Bronze support package - we will add wording later
Nice to have
• Colours - blues / blacks / grey - cyber security information and sections,
• reds etc for visualisation sections
• Use similar colours as logo for rest of pages

```html
<!DOCTYPE html>
<html lang="en">
<head>
<meta charset="utf-8">
<title>Quellora — OT Cyber Security and KPI Visualisation</title>
<link rel="stylesheet" href="https://fonts.googleapis.com/css2?family=Poppins:wght@300;400;500;600&display=swap">
<style>
:root{
  --green:#6a9f1e;
  --red:#f04a50;
  --navy:#2b3a4e;
  --card-dark:#2c3e55;
  --blue:#0255a3;
  --ink:#1b1b1b;
  --body:#474747;
  --muted:#919191;
  --line:#d3d3d3;
  --band:#eceef2;
  --white:#ffffff;
  --gold:#f2aa1c;
  --bronze:#d77a2c;
}
*{box-sizing:border-box;margin:0;padding:0}
html,body{width:1200px;height:4296px;overflow:hidden}
body{position:relative;font-family:"Poppins",sans-serif;color:var(--body);background:var(--white)}
.abs{position:absolute}
section,header,footer{position:absolute;left:0;width:1200px}

/* nav */
.site-header{top:0;height:80px;background:var(--white);z-index:2}
.brand{left:80px;top:24px;font-size:26px;font-weight:600;color:var(--ink);letter-spacing:-.5px}
.main-nav{left:300px;top:33px;display:flex;gap:26px;font-size:10.5px;font-weight:500;color:#555;letter-spacing:.4px;white-space:nowrap}
.main-nav .active{color:var(--green);position:relative}
.main-nav .active::after{content:"";position:absolute;left:50%;bottom:-22px;width:6px;height:6px;margin-left:-3px;background:var(--green);border-radius:50%}
.btn-demo{left:1028px;top:23px;width:97px;height:34px;background:var(--green);color:#fff;font-size:11px;font-weight:600;display:flex;align-items:center;justify-content:center;letter-spacing:.5px}

/* hero */
.hero{top:80px;height:642px}
.hero-photo{inset:0;background:linear-gradient(180deg,#6f7780 0%,#4c545e 45%,#2c3138 100%)}
.hero-ring{left:572px;top:235px;width:56px;height:56px;border:2px solid var(--red);border-radius:50%}
.hero-title{left:0;width:1200px;top:318px;text-align:center;color:#fff;font-size:31px;font-weight:300;line-height:1.3}
.hero-title b{font-weight:600}
.btn-outline-light{left:538px;top:473px;width:126px;height:30px;border:1px solid #fff;color:#fff;font-size:10px;font-weight:500;display:flex;align-items:center;justify-content:center;letter-spacing:.6px}

/* common */
.eyebrow{font-size:10px;font-weight:500;color:var(--muted);letter-spacing:1.2px;text-transform:uppercase}
.section-title{font-size:32px;font-weight:400;color:var(--ink)}
.section-title b{font-weight:600;color:var(--green)}
.rule{height:1px;background:var(--line)}
.lead{font-size:13px;font-weight:600;color:var(--ink);line-height:1.6}
.text{font-size:12px;line-height:1.7;color:var(--body)}
.link-more{font-size:10px;font-weight:600;color:var(--ink);letter-spacing:.6px;border-bottom:1px solid var(--ink);padding-bottom:3px}
.circle-nav{width:34px;height:34px;border-radius:50%;border:1px solid #c5c9ce;display:flex;align-items:center;justify-content:center;background:#fff}
.circle-nav.on{background:var(--green);border-color:var(--green)}

/* who */
.who{top:722px;height:724px}
.who-photo-a{left:152px;top:83px;width:358px;height:444px;background:linear-gradient(135deg,#c9d3de,#7f93aa 55%,#3e556f)}
.who-photo-b{left:435px;top:375px;width:229px;height:272px;background:linear-gradient(160deg,#5a5f66,#2c3036 60%,#a8262b)}
.who-copy{left:713px;top:145px;width:410px}
.who-copy .lead-red{font-size:13px;color:var(--ink);line-height:1.5;margin-top:20px}
.who-copy .lead-red em{font-style:normal;color:var(--red)}
.who-copy .text{margin-top:18px}

/* cyber */
.cyber{top:1446px;height:725px;background:var(--band)}
.cards{left:149px;top:229px;display:flex;gap:23px}
.svc-card{width:285px;height:341px;background:#fff;text-align:center;position:relative}
.svc-card.dark{background:var(--card-dark);color:#fff}
.svc-icon{margin:45px auto 0;width:100px;height:100px;border-radius:50%;display:flex;align-items:center;justify-content:center}
.svc-card h3{font-size:14px;font-weight:600;margin-top:34px;color:var(--ink)}
.svc-card.dark h3,.svc-card.dark .text,.svc-card.dark .link-more{color:#fff;border-color:#fff}
.svc-card .text{width:210px;margin:10px auto 0;font-size:11.5px;line-height:1.55}
.svc-card .link-more{display:inline-block;margin-top:16px}
.btn-green{background:var(--green);color:#fff;font-size:10px;font-weight:600;letter-spacing:.6px;display:flex;align-items:center;justify-content:center}

/* visualisation */
.visual{top:2171px;height:727px}
.visual-photo{left:0;top:240px;width:381px;height:404px;background:linear-gradient(135deg,#0b2440,#1c5e8a 50%,#0d1d33)}
.steps{left:435px;top:258px;width:290px}
.steps h4{font-size:12px;font-weight:600;color:var(--ink)}
.steps .text{font-size:11.5px;margin:6px 0 24px}
.manage-panel{left:765px;top:157px;width:358px;height:304px;background:var(--red);color:#fff;padding:34px 50px 30px 50px}
.manage-panel h4{font-size:13px;font-weight:600}
.manage-panel p{font-size:12.5px;line-height:1.55;margin-top:14px}

/* partners */
.partners{top:2898px;height:401px;background:var(--band)}
.logo-box{top:224px;width:230px;height:100px;background:#fff;display:flex;align-items:center;justify-content:center;gap:10px;font-size:20px;font-weight:600;color:var(--ink)}
.logo-box .mark{width:16px;height:16px;background:#555;border-radius:50%}

/* support */
.support{top:3299px;height:648px}
.pkg{top:229px;width:285px;height:333px;border:1px solid #e2e2e2;background:#fff;text-align:center}
.pkg-top{position:absolute;left:0;top:0;width:100%;height:161px}
.pkg-bar{position:absolute;left:0;top:161px;width:100%;height:34px;display:flex;align-items:center;justify-content:center;color:#fff;font-size:13px;font-weight:600}
.medal{position:absolute;left:67px;top:4px;width:150px;height:150px;border-radius:50%;border:6px solid rgba(255,255,255,.85)}
.pkg .text{position:absolute;left:40px;top:222px;width:205px;font-size:11.5px;line-height:1.5}
.pkg-btn{position:absolute;left:92px;top:278px;width:101px;height:32px;font-size:9px;font-weight:600;letter-spacing:.5px;display:flex;align-items:center;justify-content:center}

/* footer */
.site-footer{top:3947px;height:349px;background:var(--navy);color:#fff}
.site-footer h5{font-size:14px;font-weight:600}
.call{font-size:19px;font-weight:300}
.mail{font-size:12px;color:#d8dde4}
.social{display:flex;gap:10px}
.social span{width:22px;height:22px;border-radius:50%;background:#5d6a7c}
.social span.on{background:var(--green)}
.copy{font-size:11px;color:#b6bfcb}
.divider{left:487px;top:60px;width:1px;height:250px;background:#44546a}
.field{left:536px;width:438px;border-bottom:1px solid #56657a;font-size:11px;color:#cfd6df;padding-bottom:12px}
</style>
</head>
<body>

<header class="site-header">
  <div class="abs brand">Quellora</div>
  <nav class="abs main-nav">
    <span class="active">HOME</span><span>WHO WE ARE</span><span>CYBER SECURITY</span><span>VISUALISATION</span><span>TRUSTED PARTNERS</span><span>SUPPORT</span><span>CONTACT</span>
  </nav>
  <div class="abs btn-demo">LIVE DEMO</div>
</header>

<section class="hero">
  <div class="abs hero-photo" role="img" aria-label="Photo of hands on a laptop keyboard with glowing network overlay"></div>
  <div class="abs hero-ring"></div>
  <h1 class="abs hero-title">The difference between<br><b>'having data'</b> and actually knowing<br>what's going on.</h1>
  <div class="abs btn-outline-light">EXPLORE MORE</div>
</section>

<section class="who">
  <div class="abs who-photo-a" role="img" aria-label="Photo of a hand touching a shield security interface with user icons"></div>
  <div class="abs who-photo-b" role="img" aria-label="Photo of a red network cable plugged into a switch"></div>
  <div class="abs who-copy">
    <div class="eyebrow">Discover</div>
    <h2 class="section-title" style="margin-top:6px">Who <b>we</b> are</h2>
    <p class="lead-red"><em>Software</em> and <em>professional services</em> provider for Process <em>Control Cyber Security</em> and <em>Data visualisation</em></p>
    <p class="text">QT482 understands that data and networks are valuable and vulnerable so our business-critical software defines your network, the hardware, the interfaces and the protocols it carries.</p>
    <p class="text" style="margin-top:12px">We understand the core of your network how it operates and then how you need to secure your network, devices and data.</p>
    <p class="text" style="margin-top:12px">Data defines the health of your business and the state of your operations at any moment of any day.</p>
    <div style="margin-top:22px"><span class="link-more">DISCOVER MORE →</span></div>
  </div>
</section>

<section class="cyber">
  <div class="abs eyebrow" style="left:178px;top:82px">What we do</div>
  <h2 class="abs section-title" style="left:178px;top:100px">Cyber <b>Security</b></h2>
  <div class="abs rule" style="left:178px;top:152px;width:810px"></div>
  <div class="abs circle-nav" style="left:971px;top:104px"><svg width="10" height="10"><path d="M7 1 3 5l4 4" stroke="#777" fill="none" stroke-width="1.5"/></svg></div>
  <div class="abs circle-nav on" style="left:1011px;top:104px"><svg width="10" height="10"><path d="M3 1l4 4-4 4" stroke="#fff" fill="none" stroke-width="1.5"/></svg></div>
  <p class="abs lead" style="left:281px;top:164px;width:420px">Data defines the health of your business and the state of your operations at any moment of any day.</p>
  <div class="abs cards">
    <div class="svc-card">
      <div class="svc-icon" style="background:var(--blue)"><svg width="46" height="46" viewBox="0 0 46 46" fill="none" stroke="#fff" stroke-width="2"><circle cx="23" cy="23" r="16"/><ellipse cx="23" cy="23" rx="7" ry="16"/><path d="M7 23h32M10 15h26M10 31h26"/></svg></div>
      <h3>Network Security</h3>
      <p class="text">There are many variations passages of lorem ipsum avai lable, but the majority...</p>
      <span class="link-more">READ MORE →</span>
    </div>
    <div class="svc-card dark">
      <div class="svc-icon" style="background:#fff"><svg width="46" height="46" viewBox="0 0 46 46" fill="none" stroke="#2c3e55" stroke-width="2"><rect x="6" y="10" width="28" height="20" rx="2"/><path d="M14 36h12M20 30v6"/><rect x="30" y="18" width="10" height="18" rx="2"/></svg></div>
      <h3>End Point Security</h3>
      <p class="text">There are many variations passages of lorem ipsum avai lable, but the majority...</p>
      <span class="link-more">READ MORE →</span>
    </div>
    <div class="svc-card">
      <div class="svc-icon" style="background:#7a7f86"><svg width="46" height="46" viewBox="0 0 46 46" fill="none" stroke="#fff" stroke-width="2"><path d="M13 32a8 8 0 0 1 0-16 11 11 0 0 1 21 3 7 7 0 0 1-1 13z"/><rect x="19" y="23" width="9" height="7"/><path d="M21 23v-3a2.5 2.5 0 0 1 5 0v3"/></svg></div>
      <h3>Cloud Security</h3>
      <p class="text">There are many variations passages of lorem ipsum avai lable, but the majority...</p>
      <span class="link-more">READ MORE →</span>
    </div>
  </div>
  <div class="abs btn-green" style="left:541px;top:613px;width:118px;height:32px">VIEW ALL</div>
</section>

<section class="visual">
  <div class="abs eyebrow" style="left:178px;top:82px">Quellora</div>
  <h2 class="abs section-title" style="left:178px;top:100px">Visualisation</h2>
  <div class="abs rule" style="left:178px;top:152px;width:560px"></div>
  <p class="abs lead" style="left:281px;top:160px;width:440px">QT482 enables you to do that – Guard, Track, Tune, Steer – 365 days a year.</p>
  <div class="abs visual-photo" role="img" aria-label="Illustration of a digital padlock on a circuit background touched by a hand"></div>
  <div class="abs steps">
    <h4>Guard</h4>
    <p class="text">Baseline your OT communications with passive capture of your assets know your topology with confidence</p>
    <h4>Track</h4>
    <p class="text">Be alerted to any change in your baseline OT environment in real-time Pro-actively manage your threats</p>
    <h4>Tune</h4>
    <p class="text">Turn your data sources into powerful Visual Management Tools – trust your data to inform you</p>
    <span class="link-more">EXPLORE MORE →</span>
  </div>
  <div class="abs manage-panel">
    <h4>Steer</h4>
    <p>Customise and present your dashboard in minutes. Start managing, your way, in minutes, confidence.</p>
    <p>These are the core principles that QT482 delivers for your Enterprise.</p>
  </div>
</section>

<section class="partners">
  <div class="abs eyebrow" style="left:178px;top:78px">Our</div>
  <h2 class="abs section-title" style="left:178px;top:96px">Trusted <b>Partners</b></h2>
  <div class="abs rule" style="left:178px;top:148px;width:810px"></div>
  <p class="abs lead" style="left:281px;top:154px;width:470px">Contrary to popular belief, Lorem Ipsum is not simply random text. It has roots in a piece of classical Latin literature from 45 BC, making</p>
  <div class="abs logo-box" style="left:232px"><span class="mark"></span>Brevanix</div>
  <div class="abs logo-box" style="left:484px"><span class="mark"></span>Lumicore</div>
  <div class="abs logo-box" style="left:739px"><span class="mark"></span>Dorvale</div>
  <div class="abs circle-nav" style="left:1011px;top:230px"><svg width="10" height="10"><path d="M7 1 3 5l4 4" stroke="#777" fill="none" stroke-width="1.5"/></svg></div>
  <div class="abs circle-nav on" style="left:1011px;top:280px"><svg width="10" height="10"><path d="M3 1l4 4-4 4" stroke="#fff" fill="none" stroke-width="1.5"/></svg></div>
</section>

<section class="support">
  <div class="abs eyebrow" style="left:178px;top:78px">Our packages</div>
  <h2 class="abs section-title" style="left:178px;top:96px">Customer <b>Support</b></h2>
  <div class="abs rule" style="left:178px;top:148px;width:810px"></div>
  <p class="abs lead" style="left:281px;top:154px;width:470px">Contrary to popular belief, Lorem Ipsum is not simply random text. It has roots in a piece of classical Latin literature from 45 BC, making</p>

  <div class="abs pkg" style="left:152px">
    <div class="pkg-top" style="background:#dcdcdc"><div class="medal" style="background:radial-gradient(circle at 40% 35%,#f4f4f4,#a9a9a9)"></div></div>
    <div class="pkg-bar" style="background:#8f8f8f">Silver Package</div>
    <p class="text">There are many variations of passages of Lorem.</p>
    <div class="pkg-btn" style="border:1px solid #bbb;color:#999">CONTACT US</div>
  </div>
  <div class="abs pkg" style="left:458px">
    <div class="pkg-top" style="background:var(--gold)"><div class="medal" style="background:radial-gradient(circle at 40% 35%,#ffe27a,#e49a00)"></div></div>
    <div class="pkg-bar" style="background:#b9801a">Gold Package</div>
    <p class="text">There are many variations of passages of Lorem.</p>
    <div class="pkg-btn" style="background:#c98a24;color:#fff">CONTACT US</div>
  </div>
  <div class="abs pkg" style="left:765px">
    <div class="pkg-top" style="background:var(--bronze)"><div class="medal" style="background:radial-gradient(circle at 40% 35%,#f4a96a,#b45d1c)"></div></div>
    <div class="pkg-bar" style="background:#a85a1f">Bronze Package</div>
    <p class="text">There are many variations of passages of Lorem.</p>
    <div class="pkg-btn" style="border:1px solid var(--bronze);color:var(--bronze)">CONTACT US</div>
  </div>
</section>

<footer class="site-footer">
  <h5 class="abs" style="left:152px;top:64px">Contact us</h5>
  <div class="abs call" style="left:152px;top:100px">Call Us: (555) 014-2290</div>
  <div class="abs mail" style="left:152px;top:132px">hello@quellora.example</div>
  <div class="abs social" style="left:152px;top:171px"><span></span><span></span><span class="on"></span><span></span><span></span></div>
  <div class="abs copy" style="left:152px;top:262px">© 2018 – Quellora. All Rights Reserved</div>
  <div class="abs divider"></div>
  <h5 class="abs" style="left:536px;top:64px">Get in touch with us</h5>
  <div class="abs field" style="top:102px">Name</div>
  <div class="abs field" style="top:151px">Email</div>
  <div class="abs field" style="top:200px">Phone</div>
  <div class="abs btn-green" style="left:536px;top:252px;width:80px;height:31px">SEND</div>
  <svg class="abs" style="left:1012px;top:60px" width="28" height="28" viewBox="0 0 28 28" fill="none" stroke="var(--green)" stroke-width="2"><path d="M4 4h20M14 24V10M8 15l6-6 6 6"/></svg>
</footer>

</body>
</html>
```